Lantern Ridge Mentoring seeks to be a Guidance Counsellor to the World

Word Press site to be published to HostMarlo account on completion.

Basic site with integration wth Vellix Word Press Plug-in.

All simple pages to create are shown in attached power point.

LanternRidgeMentoring.com™️ seeks to be a Guidance Counsellor to the World. We help students by bringing high quality, interactive content to their virtual doorstep.

Target Market(s)

Careers

Coding

Coded - Design and coding required

Font styles to use
Sans Serif

Requirements
Must have
• Details are in powerpoint:
Registration to allow integration with Word Press Vellix Plug-in.
Nice to have
• Bright and modern feel

```html
<!DOCTYPE html>
<html lang="en">
<head>
<meta charset="utf-8">
<title>Lantern Ridge Mentoring — Home &amp; Mission</title>
<link rel="stylesheet" href="https://fonts.googleapis.com/css2?family=Questrial&family=Nunito:wght@400;800&display=swap">
<style>
  :root {
    --board: #9a9a9a;
    --sky-top: #6598c8;
    --sky-mid: #9cc0dc;
    --sky-glow: #dfe6e6;
    --indigo: #2a1c9c;
    --indigo-deep: #1d1480;
    --nav-dark: #0d0a8a;
    --nav-bright: #2c1ee0;
    --orange: #f7941d;
    --orange-light: #fbb040;
    --slate: #58585a;
    --ink: #4a4a4c;
    --white: #ffffff;
  }
  * { margin: 0; padding: 0; box-sizing: border-box; }
  html, body { width: 716px; height: 1200px; overflow: hidden; }
  body {
    background: var(--board);
    font-family: "Questrial", "Century Gothic", sans-serif;
    position: relative;
  }
  .page {
    position: absolute;
    left: 31px;
    width: 654px;
    height: 544px;
    overflow: hidden;
    border-top: 2px solid var(--orange);
    background: linear-gradient(180deg, var(--sky-top) 0%, var(--sky-top) 36%, var(--sky-mid) 50%, var(--sky-glow) 62%, var(--sky-glow) 70%);
    box-shadow: 0 6px 14px rgba(0,0,0,.35);
  }
  .page--home { top: 47px; }
  .page--mission { top: 609px; }

  .main-nav {
    position: absolute;
    left: 92px;
    top: 0;
    width: 456px;
    height: 45px;
    display: flex;
    z-index: 3;
  }
  .main-nav a {
    color: var(--white);
    text-decoration: none;
    font-size: 13px;
    display: flex;
    align-items: center;
    justify-content: center;
  }
  .nav-mission { width: 106px; background: linear-gradient(180deg, var(--orange) 0%, var(--orange-light) 100%); }
  .nav-programs { width: 125px; background: var(--nav-dark); }
  .nav-involved { width: 119px; background: linear-gradient(90deg, #0f0c96, #1610a8); }
  .nav-info { width: 106px; background: linear-gradient(90deg, #1a14c4, var(--nav-bright)); }

  .grad-photo {
    position: absolute;
    left: 0; right: 0; bottom: 0;
    height: 270px;
    background:
      radial-gradient(ellipse 70px 80px at 338px 190px, rgba(255,244,210,.95), rgba(255,220,200,.35) 55%, rgba(255,220,200,0) 100%),
      radial-gradient(ellipse 260px 140px at 338px 200px, rgba(150,130,220,.55), rgba(150,130,220,0) 100%),
      linear-gradient(180deg, rgba(42,28,156,0) 0%, rgba(42,28,156,.55) 12%, rgba(42,28,156,.85) 28%, var(--indigo) 50%, var(--indigo-deep) 100%);
  }

  .event-badge {
    position: absolute;
    left: 80px;
    top: 93px;
    width: 153px;
    height: 153px;
    border-radius: 50%;
    border: 7px solid var(--orange);
    background: var(--slate);
    color: var(--white);
    text-align: center;
    padding-top: 40px;
    z-index: 2;
  }
  .event-title { font-size: 9.5px; }
  .event-speaker { font-family: "Nunito", sans-serif; font-weight: 800; font-size: 11.5px; margin-top: 4px; }
  .event-role { font-size: 8px; margin-top: 4px; }
  .event-register {
    display: inline-block;
    margin-top: 11px;
    padding: 5px 14px;
    border: 1px solid var(--white);
    border-radius: 14px;
    font-family: "Nunito", sans-serif;
    font-weight: 800;
    font-size: 8px;
    color: var(--white);
    text-decoration: none;
  }

  .brand {
    position: absolute;
    display: flex;
    align-items: center;
    gap: 9px;
    z-index: 2;
  }
  .brand-dot { width: 18px; height: 18px; border-radius: 50%; background: var(--orange); flex: none; }
  .brand-name { color: var(--slate); font-size: 28px; line-height: 1.05; }
  .page--home .brand { left: 319px; top: 130px; }
  .page--mission .brand { left: 0; right: 0; top: 132px; justify-content: center; }

  .tagline {
    position: absolute;
    left: 319px;
    top: 229px;
    color: var(--white);
    font-size: 25px;
    font-weight: 400;
    line-height: 31px;
    z-index: 2;
  }
  .mission-text {
    position: absolute;
    left: 0; right: 0;
    top: 216px;
    text-align: center;
    color: var(--ink);
    font-size: 12.5px;
    line-height: 19px;
    z-index: 2;
  }
  .copyright {
    position: absolute;
    left: 0; right: 0;
    bottom: 16px;
    text-align: center;
    color: var(--white);
    font-size: 9px;
    z-index: 2;
  }
</style>
</head>
<body>

<section class="page page--home">
  <nav class="main-nav">
    <a class="nav-mission" href="#">Our Mission</a>
    <a class="nav-programs" href="#">Our Programs</a>
    <a class="nav-involved" href="#">Get Involved</a>
    <a class="nav-info" href="#">+info</a>
  </nav>
  <div class="grad-photo" role="img" aria-label="Silhouettes of graduates in caps and gowns holding hands raised against a sunset sky"></div>
  <div class="event-badge">
    <p class="event-title">Town Hall: “War on Viruses”</p>
    <p class="event-speaker">Dr. Maren Holt, phD</p>
    <p class="event-role">Senior Research Scientist</p>
    <a class="event-register" href="#">Register Now</a>
  </div>
  <div class="brand"><span class="brand-dot"></span><span class="brand-name">Lantern Ridge<br>Mentoring</span></div>
  <h1 class="tagline">The World’s Guidance<br>Counsellor</h1>
  <p class="copyright">© 2020 LanternRidgeMentoring . All Rights Reserved</p>
</section>

<section class="page page--mission">
  <nav class="main-nav">
    <a class="nav-mission" href="#">Our Mission</a>
    <a class="nav-programs" href="#">Our Programs</a>
    <a class="nav-involved" href="#">Get Involved</a>
    <a class="nav-info" href="#">+info</a>
  </nav>
  <div class="grad-photo" role="img" aria-label="Silhouettes of graduates in caps and gowns holding hands raised against a sunset sky"></div>
  <div class="brand"><span class="brand-dot"></span><span class="brand-name">Lantern Ridge Mentoring</span></div>
  <p class="mission-text">LanternRidgeMentoring.com™ seeks to be a Guidance Counsellor to<br>the World. We help students by bringing high quality, interactive<br>content to their virtual doorstep.</p>
  <p class="copyright">© 2020 LanternRidgeMentoring . All Rights Reserved</p>
</section>

</body>
</html>
```